Wordpress website for Dance Studio

Hi there, I am looking for Wordpress Website for dance studio. Happy for designed to use available themes. Would like a few pages setup and I can do the rest.

Other things I would like included in this theme :

Nice images page OR moving banner
Blog
Ability for youtubes

Other than that, simple requirements, just a gorgeous looking landing page/site etc.

Target Market(s)

Dance mums and kids (dancers)

Industry/Entity Type

Dance and Performancer

Coding

Coded - Design and coding required

Number of Pages Required

4 page

Font styles to use
Sans Serif

Colors
EB3D1F
EC4F4E
F09395
F8D3D4
FCEDEE

Requirements
Must have
• Wordpress theme
Nice to have
• Artistic, graphical, dance studio theme

```html
<!DOCTYPE html>
<html lang="en">
<head>
<meta charset="utf-8">
<title>Your Dance Studio – Website Template</title>
<link rel="stylesheet" href="https://fonts.googleapis.com/css2?family=Archivo:wdth,wght@62..125,100..900&family=Roboto:wght@400;500&family=Jost:wght@300;400&display=swap">
<style>
  :root{
    --canvas:#f4efe1;
    --paper:#f5f0e2;
    --footer:#f1eee8;
    --ink:#111111;
    --rule:#9a968c;
    --grey:#878787;
    --type-grey:#4a4a4a;
    --white:#ffffff;
  }
  *{box-sizing:border-box;margin:0;padding:0}
  html,body{width:1200px;height:1200px;overflow:hidden;background:var(--canvas)}
  body{position:relative;font-family:"Roboto",Arial,sans-serif;color:var(--ink)}
  .abs{position:absolute}
  .display{font-family:"Archivo",Arial,sans-serif;font-variation-settings:"wdth" 118;font-weight:500;letter-spacing:.02em;line-height:1;white-space:nowrap}
  .photo{position:absolute}
  .rule-h{position:absolute;height:1px;background:var(--rule)}
  .rule-v{position:absolute;width:1px;background:var(--rule)}
  .btn{position:absolute;background:var(--ink);color:var(--white);display:flex;align-items:center;justify-content:center}

  /* Mobile page */
  .mobile-page{left:74px;top:57px;width:422px;height:999px;background:var(--paper);box-shadow:0 14px 40px rgba(70,60,40,.28);overflow:hidden}
  .mobile-page .welcome{left:21px;top:3px;font-size:5px}
  .mobile-page .title{left:21px;top:20px;font-size:34px}
  .mobile-page .address{right:21px;top:61px;font-size:5px}
  .mobile-page .section-title{font-size:15.5px}
  .mobile-page .name{font-size:5.5px;text-align:center;width:90px}
  .mobile-page .role{font-size:3.5px;text-align:center;width:90px}
  .mobile-page .note{left:140px;top:832px;width:142px;font-size:3.2px;line-height:1.35;text-align:center}
  .mobile-footer{left:0;top:904px;width:422px;height:95px;background:var(--footer);border-top:1px solid var(--rule)}
  .mobile-footer .col{position:absolute;width:140px;text-align:center;font-size:3.5px}
  .mobile-footer .head{font-weight:500;top:26px}
  .social{display:flex;align-items:center;justify-content:center;gap:3px}
  .social i{width:4px;height:4px;border-radius:50%;background:var(--ink);display:block}

  /* Desktop panels */
  .panel{background:var(--paper);box-shadow:0 16px 38px rgba(70,60,40,.3)}
  .classes{left:193px;top:197px;width:681px;height:243px}
  .classes .heading{left:371px;top:46px;font-size:25px}
  .classes .copy{left:371px;width:195px;font-size:5.4px;line-height:8.5px}
  .shoutout{left:204px;top:478px;width:672px;height:100px}
  .shoutout .heading{left:34px;top:28px;font-size:24px}
  .shoutout .quote{left:358px;top:27px;width:156px;font-size:5px;line-height:8px}
  .shoutout .author{left:383px;top:58px;font-size:5px}
  .instructors{left:204px;top:611px;width:672px;height:274px}
  .instructors .heading{left:34px;top:35px;font-size:24.5px}
  .instructors .intro{left:396px;top:33px;width:180px;font-size:5.4px;line-height:8.5px}
  .instructor{position:absolute;top:89px}
  .instructor .photo{position:relative;height:124px}
  .instructor .name{margin-top:10px;text-align:center;font-size:8.5px}
  .instructor .role{margin-top:3px;text-align:center;font-size:5.4px}

  /* Side typography */
  .vertical{position:absolute;writing-mode:vertical-rl;transform:rotate(180deg);white-space:nowrap}
  .all-screens{left:978px;top:410px;height:398px;font-family:"Jost",sans-serif;font-weight:300;font-size:40px;letter-spacing:12.6px;color:var(--ink)}
  .devices{left:1044px;top:50px;height:758px;font-family:"Archivo",Arial,sans-serif;font-weight:800;font-variation-settings:"wdth" 100;font-size:49px;color:var(--ink)}
  .accent-line{left:853px;top:849px;width:237px;height:4px;background:var(--grey)}
  .custom-note{right:110px;top:942px;text-align:right;font-family:"Jost",sans-serif;font-weight:400;font-size:35px;line-height:44px;color:var(--type-grey);letter-spacing:.02em}
  .url-band{left:110px;top:1118px;width:980px;height:82px;background:var(--grey);display:flex;align-items:center;justify-content:center;font-family:"Jost",sans-serif;font-size:37px;color:var(--white);letter-spacing:.01em}
</style>
</head>
<body>

<!-- Mobile page -->
<section class="abs mobile-page">
  <div class="abs welcome">Welcome To</div>
  <div class="rule-h" style="left:0;top:14px;width:422px"></div>
  <h1 class="abs display title">Your Dance Studio</h1>
  <div class="rule-h" style="left:0;top:57px;width:422px"></div>
  <div class="rule-v" style="left:253px;top:57px;height:15px"></div>
  <div class="abs address">XXX Street Name, District, City</div>
  <div class="rule-h" style="left:0;top:72px;width:422px"></div>
  <div class="photo" role="img" aria-label="Dancer stretching at a ballet barre in a bright studio" style="left:0;top:72px;width:422px;height:156px;background:linear-gradient(90deg,#8d8f8a 0%,#2d2a26 25%,#5e5750 55%,#9a938a 80%,#6b655c 100%)"></div>
  <div class="photo" role="img" aria-label="Two dancers performing a duet on a wooden floor" style="left:21px;top:267px;width:97px;height:117px;background:linear-gradient(135deg,#b49a82,#6e5442 60%,#5a3f2c)"></div>
  <div class="rule-h" style="left:0;top:381px;width:422px"></div>
  <div class="rule-v" style="left:181px;top:381px;height:154px"></div>
  <div class="photo" role="img" aria-label="Aerial dance class with silks and barre" style="left:21px;top:420px;width:135px;height:114px;background:linear-gradient(160deg,#a69a86,#5d564b 55%,#3e3a33)"></div>
  <div class="abs display section-title" style="left:230px;top:410px">Our Classes</div>
  <div class="rule-h" style="left:0;top:535px;width:422px"></div>
  <div class="abs display section-title" style="left:21px;top:559px">Instructors</div>
  <div class="photo" role="img" aria-label="Portrait of an acrobatic dance instructor" style="left:21px;top:592px;width:90px;height:76px;background:linear-gradient(135deg,#ece7df,#cbb7a4 55%,#8d7663)"></div>
  <div class="photo" role="img" aria-label="Portrait of an instructor" style="left:120px;top:592px;width:9px;height:76px;background:#4a4540"></div>
  <div class="abs name" style="left:21px;top:676px">Hanna Morell</div>
  <div class="abs role" style="left:21px;top:685px">Acrobatic Dance</div>
  <div class="rule-h" style="left:0;top:708px;width:422px"></div>
  <div class="abs display section-title" style="left:21px;top:725px;line-height:.9">Students<br>Shout Out</div>
  <div class="rule-h" style="left:0;top:774px;width:422px"></div>
  <p class="abs note">Not sure if we are a good match for you or which style you want to learn? Free trial classes are available, one free class for each style. For more information, get in touch.</p>
  <div class="btn" style="left:188px;top:855px;width:45px;height:12px;font-size:3.5px">Contact Us</div>

  <footer class="abs mobile-footer">
    <div class="rule-v" style="left:141px;top:18px;height:17px"></div>
    <div class="rule-v" style="left:281px;top:18px;height:17px"></div>
    <div class="col head" style="left:0">VISIT US</div>
    <div class="col head" style="left:141px">WE'D LOVE TO DANCE WITH YOU</div>
    <div class="col head" style="left:281px">FOLLOW US</div>
    <div class="col" style="left:0;top:55px">XXX Street Name, District, City</div>
    <div class="col" style="left:141px;top:56px">(555) 014-2210</div>
    <div class="col" style="left:141px;top:67px">hello@yourstudio.example</div>
    <div class="col social" style="left:281px;top:55px"><i></i><span>Studio socials</span></div>
    <div class="col" style="left:281px;top:63px;color:#9a968c;font-size:3px">© 2021 Your Studio</div>
  </footer>
</section>

<!-- Desktop: Our Classes -->
<section class="abs panel classes">
  <div class="photo" role="img" aria-label="Dancer at the barre in an aerial silks studio" style="left:33px;top:27px;width:219px;height:186px;background:linear-gradient(150deg,#b9ad95,#7b705e 45%,#3c372f 75%,#6a5e4c)"></div>
  <div class="rule-v" style="left:292px;top:0;height:243px"></div>
  <h2 class="abs display heading">Our Classes</h2>
  <p class="abs copy" style="top:82px">Lorem ipsum dolor sit amet, consectet adipiscing elit,sed do eiusm por inciunt ut labore et dolore magna aliqua. Ut enim ad minim veniam, quis nostrud exercitation ullamco laboris nisi ut aliquip ex ea sint occaecat cupidatat non proident, sunt in culpa qui officia mollit natoque consequat massa quis enim.</p>
  <p class="abs copy" style="top:133px">Nam quam nunc, blandit vel, ridiculus mus. Donec quam Lorem ipsum dolor sit amet, consectet adipiscing elit,sed do eiusm por incididunt ut labore et dolore magna aliqua.</p>
  <div class="btn" style="left:371px;top:179px;width:74px;height:20px;font-size:5px">Learn More</div>
</section>

<!-- Desktop: Students Shout Out -->
<section class="abs panel shoutout">
  <h2 class="abs display heading" style="line-height:.9">Students<br>Shout Out</h2>
  <div class="rule-v" style="left:235px;top:0;height:100px"></div>
  <p class="abs quote">“ I'm a total beginner dancer and I felt immediately like part of the dance family.”</p>
  <div class="photo" role="img" aria-label="Student avatar" style="left:358px;top:53px;width:17px;height:17px;background:linear-gradient(135deg,#8a7f75,#3b3430)"></div>
  <div class="abs author">Noelle Ashby</div>
</section>

<!-- Desktop: Instructors -->
<section class="abs panel instructors">
  <h2 class="abs display heading">Instructors</h2>
  <p class="abs intro">Donec et pretium lorem, ac tristique massa. Nulla eu urna nisi. Nunc dignissim porta leo quis elementum. Sed laoreet felis in pretium aliquam.</p>
  <div class="instructor" style="left:34px;width:144px">
    <div class="photo" role="img" aria-label="Portrait of acrobatic dance instructor" style="width:144px;background:linear-gradient(135deg,#f0ece5,#d2bfad 50%,#a18876)"></div>
    <div class="name">Hanna Morell</div><div class="role">Acrobatic Dance</div>
  </div>
  <div class="instructor" style="left:192px;width:137px">
    <div class="photo" role="img" aria-label="Portrait of hip hop instructor" style="width:137px;background:linear-gradient(135deg,#5a4f45,#a07d68 50%,#3d3530)"></div>
    <div class="name">Pete Lindqvist</div><div class="role">Hip Hop</div>
  </div>
  <div class="instructor" style="left:343px;width:137px">
    <div class="photo" role="img" aria-label="Portrait of contemporary dance instructor" style="width:137px;background:linear-gradient(135deg,#e4e6e8,#cdb3a3 50%,#6b5a52)"></div>
    <div class="name">Kira Vale</div><div class="role">Contemporary</div>
  </div>
  <div class="instructor" style="left:494px;width:144px">
    <div class="photo" role="img" aria-label="Portrait of lyrical dance instructor" style="width:144px;background:linear-gradient(135deg,#8f7d6c,#d78aa8 40%,#7a5440 75%,#b8a89a)"></div>
    <div class="name">Nadia Osei</div><div class="role">Lyrical Dance</div>
  </div>
</section>

<!-- Side typography -->
<div class="vertical all-screens">ALL SCREENS</div>
<div class="vertical devices">MOBILE + TABLET + DESKTOP</div>
<div class="abs accent-line"></div>
<p class="abs custom-note">Colors, fonts,<br>texts &amp; images all<br>CUSTOMIZABLES</p>
<div class="abs url-band">www.studioleaf.com/dance-studio-example</div>

</body>
</html>
```